CASH PAYMENT DISCOUNT NOTICE POSTED IN CASH REGISTER AREA

LOOKING TO MAKE A FLYER OR A POSTED NOTICE FOR CUSTOMERS PAYING FOR OVER-THE-COUNTER MERCHANDISE AND WHO PAY BY CASH METHOD TO GET A 4% CASH DISCOUNT.
PRESCRIPTIONS ARE EXCLUDED FROM THIS CASH DISCOUNT.

Target Market(s)

RETAIL CUSTOMERS

Industry/Entity Type

RETAIL PHARMACY

Colors
0054AA
0677BA
7BADD7
CADEEF
E8F1F8
EB3D1F
EC4F4E
F09395
F8D3D4
FCEDEE

Requirements
Must have
• LOGO COLORS
Nice to have
• EYE CATCHING

```html
<!DOCTYPE html>
<html lang="en">
<head>
<meta charset="utf-8">
<title>Cash Discount Notice – Alderway Pharmacy</title>
<link rel="stylesheet" href="https://fonts.googleapis.com/css2?family=Oswald:wght@300;700&family=Montserrat:wght@400;600;700&display=swap">
<style>
  :root {
    --bg: #cfcfcf;
    --red-light: #ef4a4c;
    --red: #e0242d;
    --red-dark: #a8121b;
    --blue: #0054aa;
    --blue-mid: #0677ba;
    --blue-soft: #7badd7;
    --white: #ffffff;
    --ink: #111111;
    --money-light: #e9ece2;
    --money-mid: #b9c2ad;
  }
  * { box-sizing: border-box; margin: 0; padding: 0; }
  html, body { width: 1200px; height: 960px; overflow: hidden; background: var(--bg); }
  .canvas { position: relative; width: 1200px; height: 960px; }

  .flyer {
    position: absolute; left: 270px; top: 20px;
    width: 660px; height: 920px; overflow: hidden;
    background: radial-gradient(ellipse at 55% 45%, var(--red-light) 0%, var(--red) 45%, var(--red-dark) 100%);
    box-shadow: 0 6px 24px rgba(0,0,0,.25);
    font-family: 'Montserrat', sans-serif;
  }
  .flyer__frame {
    position: absolute; inset: 18px;
    border: 1.5px solid rgba(255,255,255,.85);
  }

  .headline {
    position: absolute; top: 62px; left: 0; width: 100%;
    text-align: center; color: var(--white);
    font-family: 'Oswald', sans-serif; text-transform: uppercase; line-height: 1.02;
  }
  .headline__light { display: block; font-weight: 300; font-size: 46px; letter-spacing: -1px; }
  .headline__bold { display: block; font-weight: 700; font-size: 58px; letter-spacing: -0.5px; }

  .money-art {
    position: absolute; left: 130px; top: 268px; width: 400px; height: 250px;
    border-radius: 18px;
    background: radial-gradient(ellipse at center, var(--money-light) 0%, var(--money-mid) 100%);
    opacity: .95;
  }
  .discount-band {
    position: absolute; left: 70px; top: 340px; width: 520px; height: 104px;
    background: linear-gradient(180deg, #f0393f 0%, #c3141d 100%);
    border-radius: 10px;
    box-shadow: 0 6px 14px rgba(0,0,0,.3);
    display: flex; align-items: center; justify-content: center;
    font-family: 'Oswald', sans-serif; font-weight: 700; font-size: 72px; line-height: 1;
    color: var(--white); white-space: nowrap;
  }

  .condition {
    position: absolute; right: 90px; top: 528px; text-align: right;
    font-family: 'Oswald', sans-serif; font-weight: 700; font-size: 30px;
    line-height: 1.05; color: var(--ink); text-transform: uppercase;
  }
  .cash-band {
    position: absolute; left: 70px; top: 600px; width: 370px; height: 56px;
    background: linear-gradient(90deg, var(--blue) 0%, var(--blue-mid) 100%);
    border-radius: 6px;
    display: flex; align-items: center; justify-content: center;
    font-weight: 700; font-size: 34px; color: var(--white); white-space: nowrap;
  }
  .disclaimer {
    position: absolute; left: 50px; top: 668px;
    font-size: 12px; color: var(--white); white-space: nowrap;
  }

  .contact-panel { position: absolute; inset: 0; width: 660px; height: 920px; }

  .pills-art {
    position: absolute; right: 34px; top: 640px; width: 120px; height: 60px;
    border-radius: 30px;
    background: linear-gradient(135deg, #ffffff 0%, #dfe3e8 100%);
  }
  .brand {
    position: absolute; right: 40px; top: 712px;
    display: flex; align-items: center; gap: 10px;
  }
  .brand__mark { width: 16px; height: 16px; border-radius: 50%; background: var(--blue); }
  .brand__name { font-weight: 700; font-size: 22px; color: var(--red); white-space: nowrap; }

  .address {
    position: absolute; right: 40px; top: 752px;
    display: flex; align-items: center; gap: 8px;
    font-size: 13px; font-weight: 600; color: var(--ink); white-space: nowrap;
  }
  .phone {
    position: absolute; right: 40px; top: 778px;
    display: flex; align-items: center; gap: 10px;
    font-family: 'Oswald', sans-serif; font-weight: 700; font-size: 44px; line-height: 1.2;
    color: var(--ink); white-space: nowrap;
  }
  .web, .email {
    position: absolute; right: 40px;
    display: flex; align-items: center; gap: 7px;
    font-size: 13px; font-weight: 600; color: var(--ink); white-space: nowrap;
  }
  .web { top: 846px; }
  .email { top: 872px; }
  .icon { flex: none; }
</style>
</head>
<body>
<div class="canvas">
  <section class="flyer">
    <div class="flyer__frame"></div>

    <h1 class="headline">
      <span class="headline__light">As an incentive to our</span>
      <span class="headline__bold">Customers, we now</span>
      <span class="headline__bold">Provide a</span>
    </h1>

    <div class="money-art" role="img" aria-label="Fanned hundred-dollar banknotes tied with a red ribbon"></div>
    <div class="discount-band">4% DISCOUNT</div>

    <p class="condition">On in-store<br>merchandise when</p>
    <div class="cash-band">Paying with Cash</div>
    <p class="disclaimer">* prescriptions are excluded from this cash discount</p>

    <svg class="contact-panel" viewBox="0 0 660 920" aria-hidden="true">
      <path d="M660 598 Q300 628 108 920" fill="none" stroke="var(--blue-soft)" stroke-width="16"/>
      <path d="M660 602 Q300 632 114 920" fill="none" stroke="var(--blue)" stroke-width="10"/>
      <path d="M660 610 Q300 640 120 920 L660 920 Z" fill="var(--white)"/>
    </svg>

    <div class="pills-art" role="img" aria-label="White tablets and coloured capsules"></div>

    <div class="brand">
      <span class="brand__mark"></span>
      <span class="brand__name">Alderway Pharmacy</span>
    </div>

    <p class="address">
      <svg class="icon" width="14" height="18" viewBox="0 0 14 18"><path d="M7 1a6 6 0 0 0-6 6c0 4.5 6 10 6 10s6-5.5 6-10a6 6 0 0 0-6-6z" fill="none" stroke="var(--blue)" stroke-width="1.6"/><circle cx="7" cy="7" r="2.2" fill="var(--blue)"/></svg>
      48 Alder St. Millbrook, NY 10990
    </p>

    <p class="phone">
      <svg class="icon" width="34" height="34" viewBox="0 0 24 24"><path d="M6.6 10.8a15 15 0 0 0 6.6 6.6l2.2-2.2c.3-.3.7-.4 1-.2 1.1.4 2.3.6 3.6.6.6 0 1 .4 1 1V20c0 .6-.4 1-1 1A17 17 0 0 1 3 4c0-.6.4-1 1-1h3.5c.6 0 1 .4 1 1 0 1.3.2 2.5.6 3.6.1.3 0 .7-.2 1z" fill="var(--blue)"/></svg>
      555-014-2290
    </p>

    <p class="web">
      <svg class="icon" width="18" height="18" viewBox="0 0 20 20" fill="none" stroke="var(--blue)" stroke-width="1.4"><circle cx="10" cy="10" r="8"/><ellipse cx="10" cy="10" rx="3.5" ry="8"/><path d="M2 10h16M3.5 6h13M3.5 14h13"/></svg>
      www.alderwaypharmacy.com
    </p>

    <p class="email">
      <svg class="icon" width="18" height="18" viewBox="0 0 20 20" fill="none" stroke="var(--blue)" stroke-width="1.4"><circle cx="10" cy="10" r="8.5"/><rect x="5.5" y="7" width="9" height="6.5"/><path d="M5.5 7l4.5 3.5L14.5 7"/></svg>
      alderwaypharmacy@mail.com
    </p>
  </section>
</div>
</body>
</html>
```